Kestrel Bridge Consulting (KBC) Business Card Design

I would like to create double-sided business cards that contain:
1) Name: Derek Molvane
2) Phone Number: +1 (555) 218-4907
3) Email: Derek.Molvane@KestrelBridgeConsulting.example
4) Website: KestrelBridgeConsulting.example

I would like to include my logo and a color scheme similar to the Varnholt Grand Prix Ostera squad color scheme (black, silver, greenish-blue – but can also include regular blue)

What we do: Our company develops and delivers innovative and pragmatic information technology and cybersecurity risk and compliance solutions for organizations in the commercial market as well as the federal, and state/local sectors.

```html
<!DOCTYPE html>
<html lang="en">
<head>
<meta charset="utf-8">
<title>Kestrel Bridge Consulting – Business Cards</title>
<link href="https://fonts.googleapis.com/css2?family=Source+Sans+3:wght@400;600&display=swap" rel="stylesheet">
<style>
  :root {
    --page-bg: #ececec;
    --card-white: #ffffff;
    --navy-deep: #0d1526;
    --navy-mid: #16243d;
    --brand-blue: #1f6fb3;
    --brand-sky: #2aa9e6;
    --brand-ink: #1a1f2b;
    --text-blue: #1c64a8;
    --text-light: #e9eef5;
    --text-faint: #4a5668;
  }
  * { margin: 0; padding: 0; box-sizing: border-box; }
  html, body {
    width: 1200px;
    height: 900px;
    overflow: hidden;
    background: var(--page-bg);
    font-family: "Source Sans 3", "Segoe UI", sans-serif;
  }
  .card {
    position: absolute;
    width: 504px;
    height: 290px;
    overflow: hidden;
  }
  /* Front */
  .card-front {
    left: 347px;
    top: 117px;
    background: var(--card-white);
    border: 1px solid #d6d6d6;
  }
  .front-brand {
    position: absolute;
    left: 26px;
    top: 30px;
    display: flex;
    align-items: center;
    gap: 10px;
  }
  .brand-square {
    width: 30px;
    height: 30px;
    background: var(--brand-blue);
  }
  .brand-name {
    font-weight: 600;
    text-transform: uppercase;
    letter-spacing: 0.04em;
    line-height: 1.05;
  }
  .front-brand .brand-name {
    color: var(--brand-ink);
    font-size: 14px;
  }
  .front-decoration {
    position: absolute;
    right: 0;
    top: 0;
    width: 225px;
    height: 290px;
    background: radial-gradient(circle at 75% 55%, var(--brand-sky) 0%, var(--brand-blue) 55%, rgba(31,111,179,0) 75%);
    opacity: 0.85;
  }
  .contact {
    position: absolute;
    left: 24px;
    top: 192px;
    color: var(--text-blue);
  }
  .contact-name {
    font-size: 22px;
    font-weight: 600;
    margin-left: 2px;
    margin-bottom: 8px;
  }
  .contact-line {
    font-size: 11.5px;
    line-height: 19px;
  }
  /* Back */
  .card-back {
    left: 349px;
    top: 494px;
    background: linear-gradient(90deg, var(--navy-deep) 0%, var(--navy-mid) 100%);
  }
  .back-pattern {
    position: absolute;
    right: 0;
    top: 0;
    width: 230px;
    height: 290px;
    background: radial-gradient(ellipse at 70% 40%, rgba(42,169,230,0.22) 0%, rgba(42,169,230,0) 70%);
  }
  .back-brand {
    position: absolute;
    left: 0;
    right: 0;
    top: 92px;
    display: flex;
    justify-content: center;
    align-items: center;
    gap: 14px;
  }
  .back-brand .brand-square {
    width: 44px;
    height: 44px;
    background: var(--brand-sky);
  }
  .back-brand .brand-name {
    color: var(--text-light);
    font-size: 21px;
  }
  .website {
    position: absolute;
    left: 0;
    right: 0;
    top: 213px;
    text-align: center;
    color: var(--text-light);
    font-size: 13px;
    letter-spacing: 0.02em;
  }
  .fine-print {
    position: absolute;
    left: 40px;
    right: 40px;
    top: 251px;
    text-align: center;
    color: var(--text-faint);
    font-size: 5px;
    line-height: 12.5px;
  }
</style>
</head>
<body>
  <section class="card card-front" aria-label="Business card front">
    <div class="front-brand">
      <span class="brand-square"></span>
      <span class="brand-name">Kestrel Bridge<br>Consulting</span>
    </div>
    <div class="front-decoration" role="img" aria-label="Large soft brand-colour decoration"></div>
    <div class="contact">
      <p class="contact-name">Derek Molvane</p>
      <p class="contact-line">+1 (555) 218-4907</p>
      <p class="contact-line">Derek.Molvane@KestrelBridgeConsulting.example</p>
    </div>
  </section>

  <section class="card card-back" aria-label="Business card back">
    <div class="back-pattern" role="img" aria-label="Faint glowing hexagon network pattern"></div>
    <div class="back-brand">
      <span class="brand-square"></span>
      <span class="brand-name">Kestrel Bridge<br>Consulting</span>
    </div>
    <p class="website">KestrelBridgeConsulting.example</p>
    <p class="fine-print">
      Innovative and pragmatic technology, cybersecurity risk and compliance solutions for commercial organizations.<br>
      We partner with federal, state and local agencies to plan, secure and sustain critical systems.<br>
      Practical guidance, clear reporting and dependable delivery from first assessment to lasting results.
    </p>
  </section>
</body>
</html>
```